Flyer für eine Zahnarztpraxis
Zielgruppe
Zahnarztpraxis, Zielgruppe sind Patienten im Erwachsenenalter
Aufgabenstellung
Den Text habe ich bereits geschrieben. Es soll ein DINA4 Flyer werden, mit sechs Seiten.

```html
<!DOCTYPE html>
<html lang="de">
<head>
<meta charset="utf-8">
<title>Flyer Vitamin D – Zahnarztpraxis Lindental</title>
<link href="https://fonts.googleapis.com/css2?family=Poppins:wght@400;500;600;700&display=swap" rel="stylesheet">
<style>
  :root{
    --yellow:#ece31b;
    --blush:#f8f2f4;
    --grey:#dcd9da;
    --pink:#c0577a;
    --ink:#1f1f1f;
    --logo:#4e6a6a;
    --stage:#e4e4e4;
  }
  *{box-sizing:border-box;margin:0;padding:0}
  html,body{width:706px;height:1200px;overflow:hidden}
  body{background:var(--stage);font-family:'Poppins',sans-serif;color:var(--ink);position:relative}
  .spread{position:absolute;left:20px;width:666px;height:500px;display:flex;box-shadow:0 6px 18px rgba(0,0,0,.18)}
  .spread--outside{top:60px}
  .spread--inside{top:640px}
  .panel{position:relative;width:222px;height:100%;overflow:hidden}
  .panel--blush{background:var(--blush)}
  .panel--yellow{background:var(--yellow)}
  .panel--grey{background:var(--grey)}
  .abs{position:absolute}
  h2{font-weight:600;font-size:15px;line-height:1.15}
  .rule{height:1px;background:var(--pink);width:118px;margin:5px 0 10px}
  p{font-size:7.2px;line-height:1.35}
  .strong{font-weight:600}
  .checks{list-style:none}
  .checks li{position:relative;padding-left:12px;font-size:7px;line-height:1.3;margin-bottom:5px}
  .checks li::before{content:"";position:absolute;left:0;top:1px;width:7px;height:7px;border-radius:50%;background:var(--pink)}
  .checks li::after{content:"";position:absolute;left:2px;top:2.6px;width:3px;height:1.6px;border-left:1px solid #fff;border-bottom:1px solid #fff;transform:rotate(-45deg)}
  .photo{position:absolute}
  .photo-card{position:absolute;border:4px solid #f3f0ec;border-radius:0 52px 0 34px;overflow:hidden}
  .pink{color:var(--pink);font-weight:600}
  .center{text-align:center}
  .pill{background:var(--pink);color:#fff;font-size:7.5px;font-weight:500;border-radius:3px;padding:4px 8px}
  .logo-bar{left:8px;top:0;width:214px;height:52px;background:var(--grey);border-radius:0 0 0 22px;display:flex;align-items:center;gap:8px;padding-left:16px;color:var(--logo)}
  .logo-dot{width:16px;height:16px;border-radius:50%;background:var(--logo)}
  .logo-name{font-size:8.5px;line-height:1.15;font-weight:400;letter-spacing:.4px}
  .band{left:8px;bottom:0;width:214px;height:42px;background:var(--pink);border-radius:14px 0 0 0;color:#f3e6ea;font-size:10px;font-weight:500;line-height:1.15;padding:8px 12px}
  .icon-list{list-style:none}
  .icon-list li{display:flex;align-items:center;gap:8px;font-size:7px;margin-bottom:7px;line-height:1.25}
  .icon-list li span.ic{flex:none;width:14px;height:14px;border-radius:50%;border:1px solid #4a5a5a}
</style>
</head>
<body>

<section class="spread spread--outside">
  <article class="panel panel--blush">
    <div class="abs" style="left:18px;top:30px;width:190px">
      <h2>Kennen Sie diese Situationen?</h2>
      <div class="rule"></div>
      <ul class="checks">
        <li>Kommen Sie seltener an die frische Luft, als Sie es sich wünschen?</li>
        <li>Fühlen Sie sich häufig antriebslos oder niedergeschlagen, besonders in den Wintermonaten?</li>
        <li>Haben Sie gelegentlich empfindliche Zähne oder Zahnfleischprobleme?</li>
      </ul>
      <p class="strong" style="margin-top:8px">Vielleicht steckt hinter Ihren Beschwerden ein Vitamin-D-Mangel. Mit einem Bluttest in unserer Praxis, können wir herausfinden, ob Ihrem Körper etwas fehlt</p>
      <p class="strong" style="margin-top:10px">– und unterstützen Sie bei der passenden Ergänzung.</p>
    </div>
    <div class="photo" role="img" aria-label="Hand hält Pipette mit Vitamin-D-Öl gegen die Sonne am blauen Himmel" style="left:0;top:300px;width:222px;height:200px;border-radius:0 60px 0 0;background:linear-gradient(160deg,#7fa9d8 0%,#cfe0f2 45%,#f4e3d0 70%,#c98a7a 100%)"></div>
  </article>

  <article class="panel panel--yellow">
    <div class="photo-card" role="img" aria-label="Hände formen ein Herz vor Sonnenuntergang über einer Wiese" style="left:14px;top:22px;width:196px;height:200px;background:linear-gradient(180deg,#a9c7e0 0%,#f3e8b0 40%,#e7b678 60%,#6c7a3a 100%)"></div>
    <div class="abs center" style="left:10px;top:250px;width:202px">
      <h2 style="font-size:18px;font-weight:600;line-height:1.15">Ihr Lächeln und Ihre Gesundheit sind es wert!</h2>
      <p class="strong" style="margin-top:12px">Vitamin D ist ein wichtiger Baustein für ein gesundes Leben – und gesunde Zähne.</p>
      <p class="strong" style="margin-top:8px">Unser Praxisteam berät Sie gern persönlich und beantwortet Ihre Fragen.</p>
      <p class="strong" style="margin-top:8px">Kommen Sie einfach auf uns zu – für Ihre Gesundheit von Kopf bis Fuß.</p>
    </div>
    <div class="abs pill" style="left:24px;top:438px;width:174px;text-align:center">zahnarztpraxis-lindental.de</div>
  </article>

  <article class="panel panel--yellow">
    <div class="abs logo-bar">
      <span class="logo-dot"></span>
      <span class="logo-name">ZAHNARZTPRAXIS<br>LINDENTAL &amp; TEAM</span>
    </div>
    <div class="abs center" style="left:8px;top:66px;width:206px">
      <h2 style="font-size:19px;font-weight:700;line-height:1.1">Vitamin D -<br>mehr als nur ein Sonnenvitamin</h2>
      <p style="margin-top:6px;font-size:7.5px">Was Ihre Zähne und Ihr Körper jetzt brauchen könnten</p>
    </div>
    <div class="photo-card" role="img" aria-label="Junge Frau mit Kopfhörern sitzt in der Sonne am Meer" style="left:10px;top:176px;width:140px;height:110px;border-radius:0 36px 0 26px;background:linear-gradient(180deg,#6d9fd3 0%,#c6d9ea 55%,#8a8f98 100%)"></div>
    <div class="photo-card" role="img" aria-label="Lachendes Kind" style="left:110px;top:252px;width:104px;height:84px;border-radius:0 26px 0 18px;background:linear-gradient(160deg,#f1e4d2 0%,#d9b89a 60%,#6d6d6d 100%)"></div>
    <p class="abs strong" style="left:18px;top:352px;width:130px;font-size:9.5px;line-height:1.15">Fühlen Sie sich oft müde? Haben Sie manchmal Zahnfleischprobleme oder empfindliche Zähne?</p>
    <div class="abs band">Vielleicht steckt mehr dahinter, als Sie denken...</div>
  </article>
</section>

<section class="spread spread--inside">
  <article class="panel panel--grey">
    <div class="abs" style="left:20px;top:26px;width:190px">
      <h2>Was ist Vitamin D eigentlich?</h2>
      <div class="rule"></div>
      <p>Vitamin D wird oft „Sonnenvitamin“ genannt, weil unser Körper es größtenteils selbst bildet – wenn Sonne auf unsere Haut trifft.</p>
      <p style="margin-top:7px"><span class="pink">Doch:</span> In unseren Breitengraden reicht die Sonnenstrahlung viele Monate im Jahr nicht aus, um genügend Vitamin D zu bilden.</p>
      <p style="margin-top:7px"><span class="pink">Wissen Sie wo Sie stehen?</span> Gemeinsam können wir Ihren Vitamin D Spiegel in wenigen Minuten bestimmen.</p>
    </div>
    <div class="photo" role="img" aria-label="Frau genießt mit geschlossenen Augen die Sonne am See" style="left:0;top:232px;width:222px;height:268px;border-radius:0 60px 0 0;background:linear-gradient(170deg,#3e6f7c 0%,#6f8f78 45%,#c9a08a 75%,#6b4a44 100%)"></div>
  </article>

  <article class="panel panel--yellow">
    <div class="photo-card" role="img" aria-label="Fröhliche Gruppe unterschiedlichen Alters beim High-Five nach dem Sport" style="left:12px;top:18px;width:198px;height:210px;background:linear-gradient(180deg,#8dbb5e 0%,#b7cf8a 40%,#d99c8c 70%,#5f6f8a 100%)"></div>
    <div class="abs" style="left:20px;top:246px;width:196px">
      <h2 style="font-size:14px;line-height:1.15">Warum ist Vitamin D so wichtig für den Körper?</h2>
      <div class="rule" style="background:#333;width:150px"></div>
      <ul class="checks">
        <li>Unterstützt ein starkes Immunsystem</li>
        <li>Trägt zu kräftigen Knochen bei</li>
        <li>Fördert Muskelfunktion und Gleichgewicht</li>
        <li>Kann Müdigkeit und Antriebslosigkeit entgegenwirken</li>
      </ul>
      <p style="margin-top:12px">Fehlt Vitamin D, kann das langfristig Auswirkungen auf viele Bereiche unserer Gesundheit haben – oft, ohne dass wir es sofort merken.</p>
    </div>
  </article>

  <article class="panel panel--blush">
    <div class="abs" style="left:16px;top:30px;width:196px">
      <h2>Vitamin D und Ihre Zähne – eine starke Verbindung</h2>
      <div class="pill" style="margin-top:10px;font-size:7.5px;font-weight:600;line-height:1.2;padding:5px 8px">Wussten Sie, dass Vitamin D entscheidend für gesunde Zähne ist?</div>
      <p style="margin-top:10px">Es sorgt dafür, dass Kalzium im Körper optimal aufgenommen wird – und Kalzium ist der Baustoff für feste Zähne und stabilen Kieferknochen.</p>
      <p class="strong" style="margin-top:8px;margin-bottom:7px">Ein Mangel kann unter anderem begünstigen:</p>
      <ul class="icon-list">
        <li><span class="ic"></span>Zahnfleischprobleme</li>
        <li><span class="ic"></span>Lockerung der Zähne</li>
        <li><span class="ic"></span>Schlechte Einheilung von Implantaten</li>
        <li><span class="ic"></span>Verzögerte Heilung nach zahnärztlichen Eingriffen</li>
      </ul>
    </div>
    <div class="photo" role="img" aria-label="Lachendes Seniorenpaar im herbstlichen Park" style="left:0;top:352px;width:222px;height:148px;border-radius:20px 0 0 0;background:linear-gradient(150deg,#e9b53a 0%,#d9952c 40%,#c9c2b8 65%,#7a2e34 100%)"></div>
  </article>
</section>

</body>
</html>
```